Packaging Design Job - Baby Diaper Rash Cream and Wipes Packaging Concepts Needed

Hello, Our baby brand “Mavory” is launching 2 new products – a Diaper Rash Cream and Diaper Wipes – and would like some creative design concepts for our product packaging.Mavory is a pharmaceutical brand that specializes in baby products. We are a mid – premium priced brand with a focus on targeting mothers between the ages of 18 – 35 years. Our products are positioned for mass market with other competitive brands such as Balmora, Pelvaxo, Quorel, and Lumiva, to give you a better understanding of the category. What we are looking for in our packaging is an ethical, pharmaceutical look that will appeal to mothers as a product that is safe and effective for their baby. The packaging should be clean, fresh, and consumer friendly, while still maintaining that this is a clinical product. The design concepts are a box design for the Diaper Rash Cream and a plastic packaging design for the Diaper Wipes. Attached you will find the Mavory logo and examples of Diaper Rash Cream box packaging and Diaper Wipes plastic packaging from competitors (to give you an idea of what shape of packaging we like). Please feel free to contact me should you have any questions.Thank you for your time and effort,Roska

Target Market(s)

We are a mid – premium priced brand with a focus on targeting mothers between the ages of 18 – 35 years.

Industry/Entity Type

Baby Care

Requirements
Must have
• Packaging design concepts for a box design for the Diaper Rash Cream and a plastic packaging design for the Diaper Wipes.
Nice to have
• Diaper Rash Cream box: 8 cm width, 8 cm length, 8 cm depth
• Diaper Wipes package: 23 cm width, 10.5 cm length, 4.5 cm depth

```html
<!DOCTYPE html>
<html lang="en">
<head>
<meta charset="utf-8">
<title>Mavory Diaper Rash Cream and Diaper Wipes Packaging</title>
<link rel="stylesheet" href="https://fonts.googleapis.com/css2?family=Source+Sans+3:ital,wght@0,300;0,400;0,700;1,400&display=swap">
<style>
  :root {
    --canvas: #ffffff;
    --pack-white: #ffffff;
    --pack-edge: #e4e6ea;
    --sky: #b9d3ee;
    --sky-deep: #8fb6e2;
    --sky-light: #d3e4f6;
    --blush: #f2a3b8;
    --rose: #e0245e;
    --title-blue: #3fa6de;
    --brand-navy: #17679a;
  }
  html, body {
    margin: 0;
    padding: 0;
    overflow: hidden;
    background: var(--canvas);
  }
  .canvas {
    position: relative;
    width: 1200px;
    height: 720px;
    overflow: hidden;
    background: var(--canvas);
    font-family: "Source Sans 3", sans-serif;
  }
  .pack {
    position: absolute;
    display: block;
  }
  .cream-box {
    left: 40px;
    top: 277px;
    width: 322px;
    height: 322px;
  }
  .wipes-pouch {
    left: 397px;
    top: 189px;
    width: 764px;
    height: 383px;
  }
  .panel { fill: var(--pack-white); stroke: var(--pack-edge); stroke-width: 1.5; }
  .field { fill: var(--sky); }
  .wave { fill: var(--sky-deep); }
  .wave-light { fill: var(--sky-light); opacity: 0.7; }
  .trim { fill: none; stroke: var(--blush); stroke-width: 5; }
  .brand-name {
    font-family: "Source Sans 3", sans-serif;
    font-weight: 700;
    fill: var(--brand-navy);
    letter-spacing: 2px;
  }
  .product-name {
    font-family: "Source Sans 3", sans-serif;
    font-style: italic;
    font-weight: 400;
    fill: var(--rose);
    letter-spacing: 1px;
  }
  .wipes-title {
    font-family: "Source Sans 3", sans-serif;
    font-weight: 300;
    fill: var(--title-blue);
    letter-spacing: 2px;
  }
  .wipes-claim {
    font-family: "Source Sans 3", sans-serif;
    font-weight: 400;
    fill: var(--rose);
    letter-spacing: 1px;
  }
</style>
</head>
<body>
<main class="canvas">

  <svg class="pack cream-box" viewBox="0 0 322 322" aria-label="Mavory Diaper Rash Cream box">
    <rect class="panel" x="1" y="1" width="320" height="320"/>
    <path class="field" d="M1 222 C80 232 200 228 321 192 L321 321 L1 321 Z" role="img" aria-label="Light blue dotted panel"/>
    <path class="wave-light" d="M1 262 C90 248 170 262 230 280 C270 292 300 288 321 272 L321 282 C300 300 262 304 220 290 C160 272 90 260 1 272 Z"/>
    <path class="wave" d="M1 272 C90 260 160 272 220 290 C262 304 300 300 321 282 L321 308 C290 318 250 312 205 298 C150 284 80 276 1 284 Z"/>
    <path class="trim" d="M1 222 C80 232 200 228 321 192"/>
    <text class="brand-name" x="161" y="80" text-anchor="middle" font-size="32">MAVORY</text>
    <text class="product-name" x="161" y="157" text-anchor="middle" font-size="30">Diaper Rash</text>
    <text class="product-name" x="161" y="191" text-anchor="middle" font-size="30">Cream</text>
  </svg>

  <svg class="pack wipes-pouch" viewBox="0 0 764 383" aria-label="Mavory Diaper Wipes pouch">
    <rect class="panel" x="1" y="1" width="762" height="381" rx="6"/>
    <path class="field" d="M1 160 C200 185 500 165 763 79 L763 376 Q763 382 757 382 L7 382 Q1 382 1 376 Z" role="img" aria-label="Light blue dotted panel"/>
    <path class="wave-light" d="M1 226 C150 208 300 222 430 244 C560 266 680 240 763 206 L763 218 C680 254 560 280 425 258 C300 236 150 224 1 238 Z"/>
    <path class="wave" d="M1 238 C150 224 300 236 425 258 C560 280 680 254 763 218 L763 262 C680 292 560 308 420 286 C300 266 150 250 1 256 Z"/>
    <path class="trim" d="M1 160 C200 185 500 165 763 79"/>
    <text class="wipes-title" x="382" y="104" text-anchor="middle" font-size="66">Diaper Wipes</text>
    <text class="wipes-claim" x="382" y="142" text-anchor="middle" font-size="32">ultra soft</text>
    <text class="brand-name" x="382" y="284" text-anchor="middle" font-size="39">MAVORY</text>
  </svg>

</main>
</body>
</html>
```